Tandem Tots Flyer - 2 WEEK FREE TRIAL

FLYER - We need a 1 page DL flyer with images and text. Have flyer in landscape

OFFER - 2 WEEK FREE TRIAL

HOW TO GET
Book online now at www.tandemtotsplay.com.au/booking

TAG -Where Kids are Champions

PRIZE
Chance to win Full Term of 10 weekly sessions

GIVEAWAYS
Chance to get giveaways such as tickets to games, footballs or other great offers.

LOGO - Attached

Target Market(s)

Parents of children from 5 to 16

Industry/Entity Type

Fitness

Colors
0455a3
ffc214

Requirements
Must have
• Attraction for parents to go online and sign up their kids
Should not have
• Not dull or boring

```html
<!DOCTYPE html>
<html lang="en">
<head>
<meta charset="utf-8">
<title>Tandem Tots – 2 Week Free Trial Flyer</title>
<link rel="stylesheet" href="https://fonts.googleapis.com/css2?family=Oswald:wght@500;600;700&family=Source+Sans+3:wght@400;600;700&display=swap">
<style>
  :root {
    --backdrop: #754c29;
    --brand-blue: #2b3a8f;
    --brand-blue-light: #3a4fb0;
    --brand-blue-deep: #1f2c78;
    --brand-ring: #1d4f9e;
    --brand-yellow: #ffc214;
    --brand-yellow-text: #fdd20a;
    --ink-blue: #2a3790;
    --white: #ffffff;
    --tone-hair: #7a4a32;
    --tone-skin: #e6b79c;
    --tone-skin-light: #f1d2bd;
    --tone-blonde: #e9c79a;
    --tone-soft: #f4eeea;
    --tone-laptop: #f7f7f8;
  }
  * { margin: 0; padding: 0; box-sizing: border-box; }
  html, body {
    width: 1200px; height: 696px; overflow: hidden;
    background: var(--backdrop);
  }
  .flyer {
    position: absolute; left: 88px; top: 120px;
    width: 1008px; height: 474px; overflow: hidden;
    background: var(--white);
    font-family: "Source Sans 3", Arial, sans-serif;
    box-shadow: 4px 5px 8px rgba(0,0,0,0.35);
  }
  .flyer__photo {
    position: absolute; left: 0; top: 0; width: 620px; height: 474px;
    background:
      radial-gradient(ellipse 200px 150px at 250px 470px, var(--tone-laptop) 0%, rgba(247,247,248,0.85) 55%, rgba(247,247,248,0) 100%),
      radial-gradient(ellipse 130px 170px at 370px 300px, var(--tone-blonde) 0%, rgba(233,199,154,0.6) 50%, rgba(233,199,154,0) 100%),
      radial-gradient(ellipse 150px 170px at 170px 260px, var(--tone-skin-light) 0%, var(--tone-skin) 45%, rgba(230,183,156,0) 100%),
      radial-gradient(ellipse 160px 300px at 40px 280px, var(--tone-hair) 0%, rgba(122,74,50,0.75) 45%, rgba(122,74,50,0) 100%),
      radial-gradient(ellipse 260px 160px at 80px 20px, #e3c6b0 0%, rgba(227,198,176,0) 100%),
      linear-gradient(100deg, #d8b9a3 0%, #ead7c9 45%, var(--tone-soft) 75%, var(--white) 100%);
  }
  .flyer__shapes { position: absolute; inset: 0; }
  .tagline {
    position: absolute; left: 40px; top: 22px; width: 520px;
    font-family: "Oswald", "Arial Narrow", sans-serif; font-weight: 700;
    font-size: 44px; line-height: 52px; text-align: center;
    color: var(--brand-yellow);
    text-shadow: 2px 2px 3px rgba(0,0,0,0.4);
    letter-spacing: 1.5px;
  }
  .prize {
    position: absolute; left: 416px; top: 104px; width: 170px;
    text-align: center; color: var(--ink-blue);
  }
  .prize__title { font-weight: 700; font-size: 34px; line-height: 42px; margin-bottom: 2px; }
  .prize__text { font-weight: 700; font-size: 24px; line-height: 32.5px; }
  .book-btn {
    position: absolute; left: 422px; top: 316px; width: 160px; height: 160px;
    border-radius: 50%; background: var(--white);
    display: flex; align-items: center; justify-content: center;
    box-shadow: 2px 2px 5px rgba(0,0,0,0.3);
  }
  .book-btn__ring {
    width: 150px; height: 150px; border-radius: 50%;
    background: var(--brand-ring);
    display: flex; align-items: center; justify-content: center;
  }
  .book-btn__core {
    width: 134px; height: 134px; border-radius: 50%;
    background: var(--brand-yellow);
    display: flex; align-items: center; justify-content: center;
    text-align: center; color: var(--white);
    font-family: "Oswald", "Arial Narrow", sans-serif; font-weight: 600;
    font-size: 27px; line-height: 32px;
    text-shadow: 1px 1px 2px rgba(0,0,0,0.25);
  }
  .offer {
    position: absolute; left: 640px; top: 20px; width: 340px; text-align: center;
    font-family: "Oswald", "Arial Narrow", sans-serif; font-weight: 700;
    color: var(--brand-yellow-text);
    text-shadow: 3px 3px 4px rgba(0,0,0,0.4);
  }
  .offer__line1 { display: block; font-size: 53px; line-height: 58px; letter-spacing: 1px; }
  .offer__line2 { display: block; font-size: 68px; line-height: 66px; letter-spacing: 2px; }
  .details {
    position: absolute; right: 34px; top: 168px; width: 440px;
    text-align: right; color: var(--white);
  }
  .details__heading { font-weight: 700; font-size: 22px; line-height: 28px; }
  .details__text { font-size: 19.5px; line-height: 29px; }
  .details__how { margin-top: 19px; font-size: 19.5px; line-height: 28px; color: var(--brand-yellow-text); }
  .details__url { font-weight: 700; font-size: 21.5px; line-height: 28px; }
  .brands {
    position: absolute; left: 608px; top: 390px; width: 380px;
    display: flex; justify-content: space-between;
  }
  .brand {
    display: flex; align-items: center; gap: 6px;
    font-family: "Oswald", "Arial Narrow", sans-serif; font-weight: 600;
    font-size: 21px; color: var(--brand-yellow);
    white-space: nowrap;
  }
  .brand__dot { width: 12px; height: 12px; border-radius: 50%; background: var(--brand-yellow); }
</style>
</head>
<body>
  <main class="flyer">
    <div class="flyer__photo" role="img" aria-label="Photo of a smiling mother and young daughter lying together looking at a laptop"></div>

    <svg class="flyer__shapes" width="1008" height="474" viewBox="0 0 1008 474" aria-hidden="true">
      <defs>
        <linearGradient id="panelBlue" x1="0" y1="0" x2="1" y2="1">
          <stop offset="0" stop-color="#3a4fb0"/>
          <stop offset="0.6" stop-color="#2b3a8f"/>
          <stop offset="1" stop-color="#1f2c78"/>
        </linearGradient>
        <linearGradient id="photoFade" x1="0" y1="0" x2="1" y2="0">
          <stop offset="0" stop-color="#ffffff" stop-opacity="0"/>
          <stop offset="1" stop-color="#ffffff" stop-opacity="0.95"/>
        </linearGradient>
      </defs>
      <path d="M410 0 C470 60 480 200 430 300 L360 474 L600 474 L600 0 Z" fill="url(#photoFade)"/>
      <path d="M500 0 C632 40 694 260 366 474 L1008 474 L1008 0 Z" fill="#ffc214"/>
      <path d="M516 0 C648 40 708 260 384 474 L1008 474 L1008 0 Z" fill="url(#panelBlue)"/>
    </svg>

    <h2 class="tagline">Where Kids are Champions</h2>

    <section class="prize">
      <p class="prize__title">PRIZE?</p>
      <p class="prize__text">Chance to<br>win Full Term<br>of 10 weekly<br>sessions</p>
    </section>

    <a class="book-btn">
      <span class="book-btn__ring"><span class="book-btn__core">BOOK<br>ONLINE<br>NOW</span></span>
    </a>

    <h1 class="offer">
      <span class="offer__line1">OFFER 2 WEEK</span>
      <span class="offer__line2">FREE TRIAL</span>
    </h1>

    <section class="details">
      <p class="details__heading">GIVEAWAYS</p>
      <p class="details__text">Chance to get giveaways such as tickets<br>to games, footballs or other great offers</p>
      <p class="details__how">HOW TO GET: Book online now at</p>
      <p class="details__url">www.tandemtotsplay.com.au/booking</p>
    </section>

    <div class="brands">
      <span class="brand"><span class="brand__dot"></span>Tandem Tots</span>
      <span class="brand"><span class="brand__dot"></span>Tandem Tots</span>
      <span class="brand"><span class="brand__dot"></span>Tandem Tots</span>
    </div>
  </main>
</body>
</html>
```